Halvicek Law Group, PLLC
Business card and stationery
Professional
Marcus T. Halvicek, Esq.
President
248 Perrin Avenue
Suite 3407
New York, New York 10093
mhalvicek@halviceklawgroup.example
www.halviceklawgroup.example
Using Ivory-colored card stock
There are 2 additional staff members that need cards:
nothing

```html
<!DOCTYPE html>
<html lang="en">
<head>
<meta charset="utf-8">
<title>Halvicek Law Group, PLLC — Business Card</title>
<link href="https://fonts.googleapis.com/css2?family=Montserrat:wght@400&family=Tinos:wght@400;700&display=swap" rel="stylesheet">
<style>
  :root {
    --backdrop: #e6e3de;
    --card-dark: #47474a;
    --card-dark-edge: #3a3a3c;
    --card-light: #ffffff;
    --card-silver: #d9d9db;
    --ink: #2a2a2c;
    --ink-soft: #4a4a4d;
    --logo-ink: #ffffff;
    --rule: #9a9a9d;
  }
  * { margin: 0; padding: 0; box-sizing: border-box; }
  html, body {
    width: 1200px;
    height: 1005px;
    overflow: hidden;
    background: var(--backdrop);
  }
  .canvas {
    position: relative;
    width: 1200px;
    height: 1005px;
  }
  .business-card {
    position: absolute;
    left: 100px;
    top: 185px;
    width: 1000px;
    height: 635px;
    border-radius: 30px;
    overflow: hidden;
    box-shadow: 0 18px 40px rgba(0,0,0,0.18);
  }
  .card-surface {
    position: absolute;
    inset: 0;
    width: 100%;
    height: 100%;
  }
  .firm-name {
    position: absolute;
    left: 47px;
    top: 34px;
    color: var(--logo-ink);
    font-family: "Montserrat", sans-serif;
    font-weight: 400;
    line-height: 1;
  }
  .firm-name .firm-surname {
    display: block;
    font-size: 98px;
    letter-spacing: 4px;
  }
  .firm-name .firm-entity {
    display: block;
    margin-top: 22px;
    margin-left: 150px;
    font-size: 24px;
    letter-spacing: 2px;
  }
  .holder {
    position: absolute;
    right: 545px;
    top: 432px;
    text-align: right;
    font-family: "Tinos", serif;
    color: var(--ink);
  }
  .holder-name {
    font-weight: 700;
    font-size: 27px;
  }
  .holder-title {
    margin-top: 10px;
    font-size: 22px;
    color: var(--ink-soft);
  }
  .divider {
    position: absolute;
    left: 470px;
    top: 388px;
    width: 1px;
    height: 140px;
    background: var(--rule);
  }
  .contact-list {
    position: absolute;
    left: 488px;
    top: 386px;
    list-style: none;
    font-family: "Tinos", serif;
    font-size: 22px;
    color: var(--ink);
    line-height: 1;
  }
  .contact-list li {
    display: flex;
    align-items: center;
    height: 34px;
  }
  .contact-list svg {
    width: 15px;
    height: 15px;
    margin-right: 7px;
    fill: var(--ink-soft);
    flex: none;
  }
  .contact-list .gap { margin-left: 14px; }
</style>
</head>
<body>
<main class="canvas">
  <section class="business-card" aria-label="Business card for Halvicek Law Group, PLLC">
    <svg class="card-surface" viewBox="0 0 1000 635" preserveAspectRatio="none" aria-hidden="true">
      <defs>
        <linearGradient id="lightFace" x1="0" y1="0" x2="1" y2="1">
          <stop offset="0" stop-color="var(--card-silver)"/>
          <stop offset="0.45" stop-color="var(--card-light)"/>
          <stop offset="1" stop-color="#ececed"/>
        </linearGradient>
        <linearGradient id="darkFace" x1="0" y1="0" x2="1" y2="1">
          <stop offset="0" stop-color="var(--card-dark)"/>
          <stop offset="1" stop-color="var(--card-dark-edge)"/>
        </linearGradient>
      </defs>
      <rect width="1000" height="635" fill="url(#lightFace)"/>
      <polygon points="0,0 1000,0 1000,128 0,448" fill="#c4c4c7"/>
      <polygon points="0,0 1000,0 1000,115 0,432" fill="url(#darkFace)"/>
    </svg>

    <h1 class="firm-name">
      <span class="firm-surname">HALVICEK</span>
      <span class="firm-entity">LAW GROUP, PLLC</span>
    </h1>

    <div class="holder">
      <p class="holder-name">Marcus T. Halvicek, Esq.</p>
      <p class="holder-title">President</p>
    </div>

    <div class="divider"></div>

    <ul class="contact-list">
      <li>
        <svg viewBox="0 0 16 16" aria-label="Phone"><path d="M3.2 1.5l2.3 2.6-1.3 1.9c.9 2 2.4 3.6 4.5 4.6l1.8-1.4 2.7 2.2-1.4 2.4C6.6 13.6 2.4 9.5 1 3.6z"/></svg>
        212-555-0147
        <svg class="gap" viewBox="0 0 16 16" aria-label="Fax"><rect x="4" y="1" width="8" height="5"/><rect x="1" y="6" width="14" height="7" rx="1"/><rect x="4" y="11" width="8" height="4"/></svg>
        212-555-0182
      </li>
      <li>
        <svg viewBox="0 0 16 16" aria-label="Email"><circle cx="8" cy="8" r="5"/></svg>
        mhalvicek@halviceklawgroup.example
      </li>
      <li>
        <svg viewBox="0 0 16 16" aria-label="Website"><circle cx="8" cy="8" r="5"/></svg>
        www.halviceklawgroup.example
      </li>
      <li>248 Perrin Avenue Suite 3407, New York 10093</li>
    </ul>
  </section>
</main>
</body>
</html>
```